Quillory Nest Business Card

I need a business card design. We are a collaborate online training company. Our colors are gray and green. Our website is QuilloryNest.com

I would like an area for a profile picture within the card

```html
<!DOCTYPE html>
<html lang="en">
<head>
<meta charset="utf-8">
<title>Quillory Nest Business Card</title>
<link rel="stylesheet" href="https://fonts.googleapis.com/css2?family=PT+Sans+Narrow:wght@700&family=Open+Sans:wght@400&family=Exo+2:wght@400;700&family=Crimson+Text&display=swap">
<style>
  :root {
    --backdrop: #9c9d9c;
    --card-front: #ebeceb;
    --card-back: #ffffff;
    --green-dark: #578a31;
    --green-mid: #7ab535;
    --green-light: #9ccb5a;
    --lime: #aecb1f;
    --gray-text: #77787a;
    --ink: #222222;
    --photo-top: #d9d9d9;
    --photo-bottom: #7a6d66;
  }
  * { margin: 0; padding: 0; box-sizing: border-box; }
  html, body { width: 1200px; height: 1200px; overflow: hidden; }
  body { background: var(--backdrop); position: relative; }

  .card {
    position: absolute;
    left: 176px;
    width: 848px;
    height: 472px;
    border-radius: 6px;
    overflow: hidden;
  }
  .card-front { top: 96px; background: var(--card-front); }
  .card-back { top: 631px; height: 471px; background: var(--card-back); }

  .front-stripe {
    position: absolute;
    left: 0; top: 0;
    width: 12px; height: 100%;
    background: var(--green-mid);
  }
  .front-art {
    position: absolute;
    right: 0; top: 0;
    width: 318px; height: 100%;
    background: linear-gradient(160deg, var(--green-mid) 0%, var(--green-dark) 50%, var(--lime) 100%);
  }
  .back-art {
    position: absolute;
    left: 0; top: 0;
    width: 330px; height: 100%;
    background: linear-gradient(200deg, var(--green-dark) 0%, var(--green-light) 50%, var(--lime) 100%);
  }

  .brand-name {
    position: absolute;
    left: 64px;
    top: 188px;
    font-family: "PT Sans Narrow", "Arial Narrow", sans-serif;
    font-weight: 700;
    font-size: 74px;
    line-height: 1;
    color: var(--gray-text);
    letter-spacing: -0.5px;
  }
  .front-url {
    position: absolute;
    left: 244px;
    top: 432px;
    font-family: "Open Sans", Arial, sans-serif;
    font-size: 20px;
    color: var(--green-mid);
  }

  .profile-photo {
    position: absolute;
    left: 512px;
    top: 15px;
    width: 196px;
    height: 196px;
    border-radius: 50%;
    border: 4px solid var(--green-mid);
    padding: 5px;
    background: var(--card-back);
  }
  .profile-photo-fill {
    width: 100%;
    height: 100%;
    border-radius: 50%;
    background: linear-gradient(180deg, var(--photo-top) 0%, #c9b8ad 45%, var(--photo-bottom) 100%);
  }
  .person-name {
    position: absolute;
    left: 460px;
    width: 300px;
    top: 222px;
    text-align: center;
    font-family: "Exo 2", Arial, sans-serif;
    font-weight: 700;
    font-size: 32px;
    letter-spacing: 1px;
    line-height: 1;
    color: var(--green-dark);
  }
  .person-role {
    position: absolute;
    right: 126px;
    top: 256px;
    font-family: "Exo 2", Arial, sans-serif;
    font-weight: 400;
    font-size: 20px;
    line-height: 1;
    color: var(--green-mid);
  }
  .contact-list { position: absolute; left: 419px; top: 0; list-style: none; }
  .contact-item {
    position: absolute;
    left: 0;
    display: flex;
    align-items: flex-start;
    gap: 12px;
    white-space: nowrap;
    font-family: "Crimson Text", "Times New Roman", serif;
    font-size: 26px;
    line-height: 33px;
    color: var(--ink);
  }
  .contact-phone { top: 306px; }
  .contact-address { top: 360px; }
  .contact-web { top: 430px; }
  .contact-icon {
    flex: none;
    width: 24px;
    height: 24px;
    margin-top: 5px;
  }
  .contact-address .contact-icon { margin-top: 14px; }
  .back-stripe {
    position: absolute;
    right: 0;
    top: 0;
    width: 12px;
    height: 100%;
    background: var(--green-mid);
  }
</style>
</head>
<body>

<section class="card card-front">
  <div class="front-stripe"></div>
  <div class="front-art" role="img" aria-label="Green geometric decorative artwork"></div>
  <p class="brand-name">QuilloryNest</p>
  <p class="front-url">www.quillorynest.com</p>
</section>

<section class="card card-back">
  <div class="back-art" role="img" aria-label="Green geometric decorative artwork"></div>

  <div class="profile-photo">
    <div class="profile-photo-fill" role="img" aria-label="Profile photo of the founder"></div>
  </div>
  <h1 class="person-name">Dorian Velasco</h1>
  <p class="person-role">Founder</p>

  <ul class="contact-list">
    <li class="contact-item contact-phone">
      <svg class="contact-icon" viewBox="0 0 24 24" aria-hidden="true">
        <rect width="24" height="24" rx="3" fill="var(--green-dark)"/>
        <path d="M7 5c1 0 2 2 2.5 3 .3.7-.8 1.5-1 2 .8 2 2.5 3.7 4.5 4.5.5-.2 1.3-1.3 2-1 1 .5 3 1.5 3 2.5 0 1.5-1.5 3-3 3C9.5 19 5 14.5 5 8.5 5 7 6 5 7 5z" fill="#fff"/>
      </svg>
      <span>(480) 555-0192</span>
    </li>
    <li class="contact-item contact-address">
      <svg class="contact-icon" viewBox="0 0 24 24" aria-hidden="true">
        <rect width="24" height="24" rx="3" fill="var(--green-dark)"/>
        <path d="M12 4a5 5 0 0 1 5 5c0 4-5 10-5 10S7 13 7 9a5 5 0 0 1 5-5z" fill="#fff"/>
        <circle cx="12" cy="9" r="2" fill="var(--green-dark)"/>
      </svg>
      <span>4870 E Marlow Ave. Suite 7<br>Tempe, Arizona 85281</span>
    </li>
    <li class="contact-item contact-web">
      <svg class="contact-icon" viewBox="0 0 24 24" aria-hidden="true">
        <rect width="24" height="24" rx="3" fill="var(--green-dark)"/>
        <circle cx="12" cy="12" r="7" fill="none" stroke="#fff" stroke-width="1.6"/>
        <ellipse cx="12" cy="12" rx="3" ry="7" fill="none" stroke="#fff" stroke-width="1.4"/>
        <line x1="5" y1="12" x2="19" y2="12" stroke="#fff" stroke-width="1.4"/>
      </svg>
      <span>www.quillorynest.com</span>
    </li>
  </ul>
  <div class="back-stripe"></div>
</section>

</body>
</html>
```